Fun relaxed Travel Photography Business Card*

Require a fun, funky and quirky but rememberable business card for a travel photographer

Industry/Entity Type

Photographer

Contact Information for Business Card

Front Card

(my name) Dane M.

Travel Photographer ( small under travel photographer) “self-proclaimed”

(website logo) wanderingsofdane.example

(Instagram logo) @wanderings_of_dane

(Instagram logo) @wanderings_of_dane_2.0 (backup for when Instagram puts Dane on timeout for bad behaviour)

Tel: N/A (removing the potential awkwardness of me not replying)

Email: (see above)

Back Card

Offending people since 1986

(Bottom right corner) “p.s. travelling made me fatTER”

Font styles to use
Serif

Colors

Designer to choose colors to be used in the design.

Requirements
Must have
• a camera
• a similar cartoon version of me as the "logo" see attached files, try to make as similar as possible

```html
<!DOCTYPE html>
<html lang="en">
<head>
<meta charset="utf-8">
<title>Dane M. — Travel Photographer Business Card</title>
<link rel="stylesheet" href="https://fonts.googleapis.com/css2?family=Open+Sans:wght@400;600&display=swap">
<style>
  :root {
    --backdrop: #8f7c80;
    --card-dark: #29363e;
    --panel-blue: #2b5270;
    --band-brown: #53311b;
    --accent-yellow: #e8b52f;
    --text-light: #f2f2f2;
    --shadow: rgba(40, 25, 30, 0.45);
  }
  * { margin: 0; padding: 0; box-sizing: border-box; }
  html, body {
    width: 1200px;
    height: 1200px;
    overflow: hidden;
    background: var(--backdrop);
    font-family: "Open Sans", sans-serif;
  }
  .stage {
    position: relative;
    width: 1200px;
    height: 1200px;
  }
  .card {
    position: absolute;
    left: 180px;
    width: 840px;
    height: 452px;
    background: var(--card-dark);
    box-shadow: 0 14px 30px var(--shadow);
    overflow: hidden;
  }
  .card--front { top: 110px; }
  .card--back { top: 638px; }

  /* Front */
  .info-panel {
    position: absolute;
    top: 0;
    right: 0;
    width: 403px;
    height: 100%;
    background: var(--panel-blue);
  }
  .name-band {
    position: absolute;
    top: 26px;
    left: 0;
    width: 100%;
    height: 110px;
    background: var(--band-brown);
    padding: 20px 0 0 48px;
    color: var(--text-light);
  }
  .name {
    color: var(--accent-yellow);
    font-size: 29px;
    font-weight: 400;
    letter-spacing: 1px;
    line-height: 1.1;
  }
  .title {
    font-size: 21px;
    line-height: 1.2;
    text-transform: uppercase;
  }
  .title-note {
    font-size: 14px;
    line-height: 1.2;
    padding-left: 22px;
  }
  .contacts {
    position: absolute;
    left: 18px;
    bottom: 36px;
    list-style: none;
    color: var(--text-light);
    font-size: 15px;
  }
  .contacts li {
    display: flex;
    align-items: center;
    gap: 8px;
    line-height: 26px;
  }
  .contacts svg { flex: none; }
  .mascot {
    position: absolute;
    left: 110px;
    top: 80px;
    width: 230px;
    height: 300px;
    border-radius: 18px;
    background: linear-gradient(160deg, #f0b733 0%, #d79a25 55%, #7a4a2a 100%);
  }

  /* Back */
  .slogan {
    position: absolute;
    top: 50%;
    left: 0;
    width: 100%;
    transform: translateY(-50%);
    text-align: center;
    color: var(--accent-yellow);
    font-size: 35px;
    font-weight: 400;
    letter-spacing: 0.5px;
  }
  .postscript {
    position: absolute;
    right: 44px;
    bottom: 60px;
    color: var(--accent-yellow);
    font-size: 18px;
  }
</style>
</head>
<body>
<main class="stage">
  <section class="card card--front" aria-label="Business card front">
    <div class="mascot" role="img" aria-label="Cartoon mascot of Dane lounging on a yellow deck chair with a drink"></div>
    <div class="info-panel">
      <div class="name-band">
        <h1 class="name">DANE M.</h1>
        <p class="title">Travel Photographer</p>
        <p class="title-note">self-proclaimed</p>
      </div>
      <ul class="contacts">
        <li>
          <svg width="14" height="14" viewBox="0 0 14 14" aria-hidden="true"><circle cx="7" cy="7" r="6" fill="none" stroke="#f2f2f2" stroke-width="1.5"/><path d="M1 7h12M7 1c-3 3-3 9 0 12M7 1c3 3 3 9 0 12" fill="none" stroke="#f2f2f2" stroke-width="1.2"/></svg>
          wanderingsofdane.example
        </li>
        <li>
          <svg width="14" height="14" viewBox="0 0 14 14" aria-hidden="true"><rect x="1" y="1" width="12" height="12" rx="2" fill="#f2f2f2"/></svg>
          @wanderings_of_dane
        </li>
        <li>
          <svg width="14" height="14" viewBox="0 0 14 14" aria-hidden="true"><rect x="1" y="1" width="12" height="12" rx="2" fill="#f2f2f2"/></svg>
          @wanderings_of_dane_2.0
        </li>
      </ul>
    </div>
  </section>

  <section class="card card--back" aria-label="Business card back">
    <p class="slogan">OFFENDING PEOPLE SINCE 1986</p>
    <p class="postscript">p.s. travelling made me fatTER</p>
  </section>
</main>
</body>
</html>
```